Brightwell Systems - Company Overview Brochure

We would like a single page A4 Brochure to give to new potential customers to provide a quick overview of our company. This will be used in presales meetings.

We have included the content we would like on the brochure under "Brightwell Systems Marketing Brochure.docx".

We have included two other designs "timebundleterms v4.pdf and Brightwell Public Cloud Plans.pdf" which shows similar marketing brochures we have. We would like these designs to have the same Brightwell Blue and "Specialised Technology Consultancy firm" theme.

Target Market(s)

Technology Sector

Industry/Entity Type

Information Technology

Colors
0054AA
0677BA
7BADD7
CADEEF
E8F1F8

Requirements
Must have
• "Innovative Tech Company Theme".

```html
<!DOCTYPE html>
<html lang="en">
<head>
<meta charset="utf-8">
<title>Brightwell Systems – Company Overview</title>
<link rel="stylesheet" href="https://fonts.googleapis.com/css2?family=Merriweather:ital,wght@0,300;0,400;0,700;0,900;1,400;1,700;1,900&display=swap">
<style>
  :root{
    --stage:#8f8f8f;
    --page:#0b1428;
    --page-deep:#08101f;
    --navy-card:#12306f;
    --navy-card-edge:#2a4d98;
    --brand-blue:#0054aa;
    --bright-blue:#0677ba;
    --sky:#7badd7;
    --mist:#cadeef;
    --ice:#e8f1f8;
    --label:#8fa6cc;
    --rule:#1d2a47;
    --muted:#b6c3d8;
  }
  *{box-sizing:border-box;margin:0;padding:0}
  html,body{width:1200px;height:2400px;overflow:hidden;background:var(--stage)}
  body{font-family:"Merriweather",Georgia,serif;position:relative}
  .brochure{position:absolute;left:0;top:344px;width:1200px;height:1712px;background:linear-gradient(180deg,#0c1630 0%,var(--page) 55%,var(--page-deep) 100%);overflow:hidden;color:var(--ice)}
  .abs{position:absolute}
  .brand{left:72px;top:160px;display:flex;align-items:center;gap:18px}
  .brand-square{width:34px;height:34px;background:var(--brand-blue)}
  .brand-name{font-size:38px;font-weight:700;color:var(--bright-blue);letter-spacing:1px}
  .brand-decor{left:740px;top:0;width:460px;height:360px;background:radial-gradient(ellipse at 60% 45%,rgba(0,84,170,.75) 0%,rgba(0,84,170,.25) 45%,rgba(11,20,40,0) 72%)}
  .top-rule{left:72px;top:263px;width:700px;height:1px;background:var(--rule)}
  .tagline-band{left:0;top:280px;width:760px;height:76px;background:linear-gradient(90deg,#1c3f8f 0%,#163272 55%,rgba(11,20,40,0) 100%);display:flex;align-items:center;padding-left:72px}
  .tagline-band::before{content:"";width:4px;height:30px;background:var(--sky);margin-right:20px}
  .tagline-band span{font-style:italic;font-weight:900;font-size:30px;color:var(--sky);letter-spacing:3px}
  .accent-line{left:72px;top:406px;width:92px;height:4px;background:linear-gradient(90deg,var(--bright-blue),rgba(6,119,186,0))}
  .intro{left:72px;top:440px;width:1000px;font-size:23px;line-height:36px;color:var(--ice);font-weight:300}
  .eyebrow{font-size:16px;letter-spacing:6px;color:var(--label);text-transform:uppercase}
  .services-label{left:72px;top:566px}
  .services-rule{left:72px;top:634px;width:1056px;height:1px;background:var(--rule)}
  .group-label{font-size:17px;letter-spacing:4px;color:var(--mist);text-transform:uppercase}
  .group-it{left:54px;top:670px}
  .group-esc{left:54px;top:864px}
  .service-row{left:54px;display:flex;gap:20px}
  .row-it{top:700px}
  .row-esc{top:894px}
  .service-card{width:247px;height:136px;background:linear-gradient(180deg,#16397f 0%,var(--navy-card) 100%);border:1px solid var(--navy-card-edge);border-top:3px solid #2c58b0;border-radius:3px;display:flex;flex-direction:column;align-items:center;justify-content:center;gap:8px;text-align:center}
  .service-card.wide{width:280px}
  .service-icon{width:44px;height:44px}
  .service-name{font-size:19px;font-weight:700;line-height:26px;color:var(--ice)}
  .mid-rule{left:72px;top:1073px;width:1056px;height:1px;background:var(--rule)}
  .col-commit{left:69px;top:1104px;width:490px}
  .col-policy{left:644px;top:1104px;width:490px}
  .col-rule{height:1px;background:var(--rule);margin:14px 0 16px}
  .commit-text{font-size:22px;line-height:33px;color:var(--ice);font-weight:300}
  .policy-title{font-size:21px;font-weight:700;color:var(--ice);margin-bottom:6px}
  .policy-text{font-size:20px;line-height:29px;color:var(--muted);font-weight:300;margin-bottom:24px}
  .col-divider{left:602px;top:1104px;width:1px;height:260px;background:var(--rule)}
  .network-field{left:0;top:1380px;width:1200px;height:332px;background:radial-gradient(ellipse at 35% 40%,rgba(6,119,186,.22) 0%,rgba(11,20,40,0) 60%),radial-gradient(ellipse at 80% 70%,rgba(0,84,170,.18) 0%,rgba(11,20,40,0) 55%)}
  .motto-band{left:63px;top:1419px;width:690px;height:92px;background:linear-gradient(90deg,#21489a 0%,#183878 60%,rgba(11,20,40,0) 100%);display:flex;align-items:center;padding-left:100px;gap:26px}
  .motto-band .first{font-style:italic;font-weight:700;font-size:42px;color:var(--sky)}
  .motto-band .second{font-style:italic;font-weight:900;font-size:44px;color:var(--ice)}
  .contact{left:54px;top:1548px;border-left:3px solid #2c58b0;padding-left:24px}
  .contact .web{font-size:19px;color:var(--sky);line-height:30px}
  .contact .place{font-size:16px;color:var(--muted);line-height:28px}
  .sign-off{right:52px;top:1556px;font-style:italic;font-size:18px;color:var(--sky)}
  .bottom-rule{left:0;top:1651px;width:1200px;height:1px;background:var(--rule)}
</style>
</head>
<body>
<main class="brochure">
  <div class="abs brand-decor" role="img" aria-label="Large brand mark glow decoration"></div>

  <div class="abs brand"><span class="brand-square"></span><span class="brand-name">Brightwell Systems</span></div>
  <div class="abs top-rule"></div>

  <div class="abs tagline-band"><span>" Specialised Consulting "</span></div>

  <div class="abs accent-line"></div>
  <p class="abs intro">Brightwell Systems delivers specialised consulting with Perth's finest engineers — combining deep technical expertise with a commitment to getting it right the first time.</p>

  <h2 class="abs eyebrow services-label">Our Services</h2>
  <div class="abs services-rule"></div>

  <h3 class="abs group-label group-it">IT Services</h3>
  <div class="abs service-row row-it">
    <div class="service-card">
      <svg class="service-icon" viewBox="0 0 44 44"><circle cx="22" cy="22" r="21" fill="#1f4fa8"/><path d="M14 18h5a3 3 0 1 1 6 0h5v5a3 3 0 1 0 0 6v5H14v-5a3 3 0 1 0 0-6z" fill="#fff"/></svg>
      <div class="service-name">Project<br>Integration</div>
    </div>
    <div class="service-card">
      <svg class="service-icon" viewBox="0 0 44 44"><circle cx="22" cy="22" r="21" fill="#1f4fa8"/><path d="M10 20l6-5 6 3 6-3 6 5-8 8-4-3-4 3z" fill="#fff"/></svg>
      <div class="service-name">Managed<br>Services</div>
    </div>
    <div class="service-card">
      <svg class="service-icon" viewBox="0 0 44 44"><circle cx="22" cy="22" r="21" fill="#1f4fa8"/><path d="M17 20v-4a5 5 0 0 1 10 0v4" fill="none" stroke="#fff" stroke-width="3"/><rect x="14" y="20" width="16" height="13" rx="2" fill="#fff"/></svg>
      <div class="service-name">Enterprise<br>Security</div>
    </div>
    <div class="service-card wide">
      <svg class="service-icon" viewBox="0 0 44 44"><circle cx="22" cy="22" r="21" fill="#1f4fa8"/><circle cx="22" cy="22" r="8" fill="none" stroke="#fff" stroke-width="5" stroke-dasharray="4 2.3"/><circle cx="22" cy="22" r="4" fill="#1f4fa8" stroke="#fff" stroke-width="2"/></svg>
      <div class="service-name">Software<br>Development</div>
    </div>
  </div>

  <h3 class="abs group-label group-esc">Electronic Security &amp; Communications</h3>
  <div class="abs service-row row-esc">
    <div class="service-card">
      <svg class="service-icon" viewBox="0 0 44 44"><circle cx="22" cy="22" r="21" fill="#1f4fa8"/><path d="M11 17l20-5 2 7-20 5z" fill="#fff"/><path d="M22 22v7h-8" fill="none" stroke="#fff" stroke-width="2.5"/></svg>
      <div class="service-name">CCTV</div>
    </div>
    <div class="service-card">
      <svg class="service-icon" viewBox="0 0 44 44"><circle cx="22" cy="22" r="21" fill="#1f4fa8"/><path d="M22 10l10 4v7c0 6-4 10-10 13-6-3-10-7-10-13v-7z" fill="none" stroke="#fff" stroke-width="2.5"/><path d="M17 22l4 4 6-7" fill="none" stroke="#fff" stroke-width="2.5"/></svg>
      <div class="service-name">Integrated Electronic<br>Security</div>
    </div>
    <div class="service-card">
      <svg class="service-icon" viewBox="0 0 44 44"><circle cx="22" cy="22" r="21" fill="#1f4fa8"/><path d="M13 32c4-8 8-14 17-19M15 33c5-7 9-11 17-14M17 34c5-5 9-8 16-9" fill="none" stroke="#fff" stroke-width="2"/></svg>
      <div class="service-name">Structured Cabling<br>&amp; Fibre Optics</div>
    </div>
    <div class="service-card wide">
      <svg class="service-icon" viewBox="0 0 44 44"><circle cx="22" cy="22" r="21" fill="#1f4fa8"/><circle cx="22" cy="18" r="2.5" fill="#fff"/><path d="M22 20l-5 14M22 20l5 14" stroke="#fff" stroke-width="2"/><path d="M15 12a9 9 0 0 0 0 12M29 12a9 9 0 0 1 0 12M18 14a5 5 0 0 0 0 8M26 14a5 5 0 0 1 0 8" fill="none" stroke="#fff" stroke-width="1.8"/></svg>
      <div class="service-name">Wireless<br>Communications</div>
    </div>
  </div>

  <div class="abs mid-rule"></div>

  <section class="abs col-commit">
    <h2 class="eyebrow">Our Commitment</h2>
    <div class="col-rule"></div>
    <p class="commit-text">We do things right the first time — fair, but<br>never cheap. Serving government &amp; enterprise<br>with solutions aligned to vendor best practices.<br>In cybersecurity &amp; continuity, no shortcut<br>is worth taking.</p>
  </section>
  <div class="abs col-divider"></div>
  <section class="abs col-policy">
    <h2 class="eyebrow">Our Policy</h2>
    <div class="col-rule"></div>
    <h3 class="policy-title">Be Fair</h3>
    <p class="policy-text">Both parties benefit when pricing is<br>balanced — protecting quality and<br>sustaining long-term relationships.</p>
    <h3 class="policy-title">Be Cost-Effective</h3>
    <p class="policy-text">High quality at a fair cost, through<br>intelligent, efficient delivery.</p>
  </section>

  <div class="abs network-field" role="img" aria-label="Faint glowing network of connected points"></div>

  <div class="abs motto-band"><span class="first">Do it Once,</span><span class="second">Do it Right</span></div>

  <div class="abs contact">
    <div class="web">brightwellsystems.com.au</div>
    <div class="place">Perth, Western Australia · T&amp;C: brightwellsystems.com.au/t&amp;c</div>
  </div>
  <div class="abs sign-off">" Specialised Consulting "</div>
  <div class="abs bottom-rule"></div>
</main>
</body>
</html>
```